K M Guard Solutions - Alarm and CCTV installation Flyer

Need a flyer designed that grabs the attention of potential customers, we need the price to stand out the most to grab people’s attention, whether they are residential or commercial.We are a security company based in Brentwood Essex but cover London and the home counties. here is our website to take a look at www.kmguardsolutions.co.uk. We want them to know we install complete alarm and Cctv systems and will keep them “safe”

Target Market(s)

residential and commercial property

Colors
f37122

Requirements
Must have
• on one side
• large clear logo - professional design
• - Intruder Alarms starting from £495 + VAT. (Big text)
• - £150 discount on installations
• *terms and conditions apply (small text)
• - Not happy with your current provider? Free of charge no obligation take over survey and quotation and up to £100 off
• - CCTV systems starting from £595 + VAT (based on 2 cameras)
• K M Guard Solutions are always there, always available, wherever and whenever you need us.
• Large telephone number at the bottom 01632 480913
• Address / email / website as a footer * see website for details
• on second side
• large and bold
• Are you looking to keep you and your premises safe?
• - K M Guard Solutions install, maintain and repair all intruder alarms, CCTV, intercom and access control
• - View, control and manage your security systems anywhere in the world
• - Feel at ease with monitoring services & police response tailored to suit you and your business
• - K M Guard can takeover any existing security system and offer maintenance checks to guarantee the best performance for you and your premises
• - K M Guard understand that being security conscious is ever increasing, protecting your property and family is a number one priority
• - Our fully insured and accredited team offer quality, safety and cost efficiency throughout the whole process
• - K M Guard Solutions are using the latest cloud-based technology to stay connected with your home and business 24/7
• If you are looking to improve the security in your home, office or commercial property then call a member of our team today for a free quote.
• Fully insured and accredited
• Tradevouch logo and NQPB Intruder and CCTV logos
• Logo somewhere on page and
• Telephone number
• Address / email / website as footer
Nice to have
• We would like to have the text saying
• Intruder alarms installed from £495 + vat the biggest text on the page. Most likely the £495 part the largest.
• Also would like “not happy with your current provider” more obvious
• We would like use our company colours - Orange/White/black

```html
<!DOCTYPE html>
<html lang="en">
<head>
<meta charset="utf-8">
<title>K M Guard Solutions – Alarm and CCTV Flyer</title>
<link href="https://fonts.googleapis.com/css2?family=Bebas+Neue&family=Hind:wght@400;500;600&family=Montserrat:wght@500;600&display=swap" rel="stylesheet">
<style>
  :root {
    --orange: #f37122;
    --orange-deep: #e8501f;
    --ink: #2b2b2b;
    --text: #555555;
    --panel: #e9e9ea;
    --panel-light: #efeff0;
    --white: #ffffff;
    --page: #e6e4e1;
  }
  * { box-sizing: border-box; margin: 0; padding: 0; }
  html, body { width: 1200px; height: 801px; overflow: hidden; }
  body { background: var(--page); font-family: "Hind", Arial, sans-serif; position: relative; }

  .flyer {
    position: absolute; top: 58px; width: 484px; height: 685px;
    background: var(--white); overflow: hidden;
    box-shadow: 0 4px 14px rgba(0,0,0,.18);
  }
  .flyer--front { left: 72px; }
  .flyer--back { left: 644px; }

  /* Brand block */
  .brand {
    position: absolute; top: 0; width: 240px; height: 108px; background: var(--white);
    display: flex; flex-direction: column; align-items: center; justify-content: center; gap: 4px;
    z-index: 3;
  }
  .flyer--front .brand { left: 0; clip-path: polygon(0 0, 100% 0, 76% 100%, 0 100%); padding-right: 56px; }
  .flyer--back .brand { right: 0; clip-path: polygon(0 0, 100% 0, 100% 100%, 24% 100%); padding-left: 56px; }
  .brand__mark { width: 30px; height: 30px; background: var(--orange); }
  .brand__name {
    font-family: "Montserrat", Arial, sans-serif; font-weight: 600; color: var(--orange);
    font-size: 17px; line-height: 1.05; text-align: center; letter-spacing: .5px;
  }

  /* Image placeholders */
  .photo { position: absolute; }
  .photo--front-hero {
    left: 0; top: 0; width: 484px; height: 325px;
    background: linear-gradient(135deg, #d9d7d3 0%, #b9b6b1 45%, #7d7a76 100%);
    clip-path: polygon(0 0, 100% 0, 100% 88%, 52% 99%, 0 89%);
  }
  .photo--phones {
    left: 258px; top: 176px; width: 212px; height: 222px; border-radius: 14px;
    background: linear-gradient(160deg, #2d7fc4 0%, #49a7e3 50%, #f2f4f6 100%);
    z-index: 2;
  }
  .photo--back-hero {
    left: 0; top: 0; width: 484px; height: 265px;
    background: linear-gradient(120deg, #cfe0ec 0%, #b8c0c6 40%, #d7cdbd 100%);
  }
  .stripes { position: absolute; left: 0; top: 0; z-index: 1; }

  /* Front copy */
  .headline {
    position: absolute; left: 22px; top: 350px; width: 228px;
    font-family: "Bebas Neue", Impact, sans-serif; font-weight: 400; font-size: 25px; line-height: 1.08;
    color: #3a3a3a; white-space: nowrap;
  }
  .offer {
    position: absolute; left: 22px; top: 414px; font-size: 13px; color: var(--orange-deep);
  }
  .prices {
    position: absolute; left: 0; top: 451px; width: 484px; height: 147px; background: var(--panel);
    display: grid; grid-template-columns: repeat(3, 1fr);
    box-shadow: 0 3px 6px rgba(0,0,0,.12);
  }
  .price {
    display: flex; flex-direction: column; align-items: center; padding-top: 20px;
    text-align: center; color: #666; font-size: 12.5px; line-height: 1.2;
  }
  .price + .price { border-left: 1px dotted #b5b5b5; margin: 14px 0; padding-top: 6px; }
  .price svg { height: 56px; margin-bottom: 12px; }
  .price small { font-size: 9.5px; }
  .tagline {
    position: absolute; left: 0; width: 100%; top: 618px; text-align: center;
    font-size: 11.5px; color: var(--orange-deep);
  }

  /* Footer */
  .footer { position: absolute; left: 0; bottom: 0; width: 100%; height: 45px; background: var(--ink); }
  .footer__band {
    position: absolute; right: 0; top: 0; width: 312px; height: 100%; background: var(--orange-deep);
    clip-path: polygon(0 0, 100% 0, 100% 100%, 6% 100%);
    color: var(--white); text-align: right; padding: 7px 10px 0 0; font-size: 9.6px; line-height: 1.55;
  }
  .footer__address { font-size: 8.4px; }
  .footer__phone {
    position: absolute; left: 16px; top: 12px; display: flex; align-items: center; gap: 6px;
    font-family: "Montserrat", Arial, sans-serif; font-weight: 500; font-size: 17px; letter-spacing: 1.3px;
    color: var(--white);
  }

  /* Back copy */
  .question {
    position: absolute; left: 0; top: 270px; width: 100%; height: 62px; background: var(--orange-deep);
    display: flex; align-items: center; justify-content: center;
    font-family: "Bebas Neue", Impact, sans-serif; font-weight: 400; font-size: 24px; color: var(--white); letter-spacing: .2px;
  }
  .services {
    position: absolute; left: 0; top: 338px; width: 100%; height: 214px; background: var(--panel-light);
    list-style: none; padding: 12px 18px 0 20px;
  }
  .services li {
    display: flex; gap: 6px; font-size: 10px; line-height: 1.3; color: #444; margin-bottom: 6px;
  }
  .services svg { flex: 0 0 13px; height: 13px; margin-top: 1px; }
  .accreditation {
    position: absolute; left: 0; top: 562px; width: 100%; display: flex; justify-content: center; align-items: center; gap: 14px;
  }
  .listing { font-family: "Hind", Arial, sans-serif; font-weight: 600; font-size: 15px; color: var(--orange-deep); }
  .badge { width: 22px; height: 22px; border-radius: 50%; border: 2px solid #3a5a8a; }
  .badge--square { border-radius: 2px; }
  .callout {
    position: absolute; left: 0; top: 606px; width: 100%; text-align: center;
    font-size: 11.5px; line-height: 1.3; color: var(--orange-deep);
  }
</style>
</head>
<body>

<!-- Front side -->
<section class="flyer flyer--front">
  <div class="photo photo--front-hero" role="img" aria-label="Photo of an alarm keypad in front of a staircase with a CCTV camera"></div>
  <svg class="stripes" width="484" height="340" viewBox="0 0 484 340" aria-hidden="true">
    <polygon points="0,287 0,300 252,331 252,319" fill="var(--orange-deep)"/>
    <polygon points="440,298 484,288 484,297 444,306" fill="var(--orange-deep)"/>
  </svg>
  <div class="photo photo--phones" role="img" aria-label="Two smartphones showing a security system control app"></div>

  <header class="brand">
    <span class="brand__mark"></span>
    <span class="brand__name">K M GUARD<br>SOLUTIONS</span>
  </header>

  <h1 class="headline">Not happy with<br>your current provider?</h1>
  <p class="offer">Free of charge no obligation take over survey and quotation and up to £100 off</p>

  <div class="prices">
    <div class="price">
      <svg viewBox="0 0 64 56" aria-hidden="true">
        <rect x="22" y="6" width="20" height="44" rx="5" fill="var(--orange-deep)"/>
        <rect x="26" y="14" width="12" height="12" rx="2" fill="#fff"/>
        <path d="M15 14 q-7 14 0 28 M8 10 q-10 18 0 36 M49 14 q7 14 0 28 M56 10 q10 18 0 36" stroke="var(--orange-deep)" stroke-width="3" fill="none" stroke-linecap="round"/>
      </svg>
      <span>Intruder Alarms<br>starting from<br>£495 + VAT</span>
    </div>
    <div class="price">
      <svg viewBox="0 0 64 64" aria-hidden="true">
        <g fill="var(--orange-deep)">
          <circle cx="24" cy="38" r="15"/>
          <circle cx="44" cy="18" r="11"/>
        </g>
        <g stroke="var(--orange-deep)" stroke-width="6" stroke-linecap="round">
          <path d="M24 18v-2M24 58v2M4 38h-0M44 38h2M10 24l-1-1M38 52l1 1M10 52l-1 1M38 24l1-1"/>
          <path d="M44 3v1M44 33v0M29 18h0M59 18h0M33 7l0 0M55 29l0 0M33 29l0 0M55 7l0 0"/>
        </g>
        <circle cx="24" cy="38" r="6" fill="var(--panel)"/>
        <circle cx="44" cy="18" r="4.5" fill="var(--panel)"/>
      </svg>
      <span>£150 discount on<br>installations<br><small>*terms and conditions<br>apply</small></span>
    </div>
    <div class="price">
      <svg viewBox="0 0 72 60" aria-hidden="true">
        <path d="M6 10 L50 18 L46 34 L4 24 Z" fill="var(--orange-deep)"/>
        <rect x="50" y="18" width="8" height="10" fill="var(--orange-deep)"/>
        <path d="M30 30 L38 44 H58" stroke="var(--orange-deep)" stroke-width="6" fill="none"/>
        <rect x="58" y="30" width="7" height="26" fill="var(--orange-deep)"/>
      </svg>
      <span>CCTV systems starting<br>from £595 + VAT<br>(based on 2 cameras)</span>
    </div>
  </div>

  <p class="tagline">K M Guard Solutions are always there, always available, wherever and whenever you need us.</p>

  <footer class="footer">
    <div class="footer__phone">
      <svg width="18" height="18" viewBox="0 0 24 24" aria-hidden="true"><circle cx="12" cy="12" r="10.5" fill="none" stroke="#fff" stroke-width="1.8"/><path d="M8.2 6.5l2 2.2-1.1 1.6c.8 1.7 2 2.9 3.7 3.7l1.6-1.1 2.2 2-1.3 2c-4.4-.4-8.1-4.1-8.5-8.5z" fill="#fff"/></svg>
      01632 480913
    </div>
    <div class="footer__band">
      <div>operations@kmguardsolutions.co.uk &nbsp;|&nbsp; www.kmguardsolutions.co.uk</div>
      <div class="footer__address">14 Harlow Lane, Brentwood, Essex, CM14 9QX</div>
    </div>
  </footer>
</section>

<!-- Back side -->
<section class="flyer flyer--back">
  <div class="photo photo--back-hero" role="img" aria-label="Photo of a wall-mounted security touch panel in a modern kitchen"></div>

  <header class="brand">
    <span class="brand__mark"></span>
    <span class="brand__name">K M GUARD<br>SOLUTIONS</span>
  </header>

  <h2 class="question">Are you looking to keep you and your premises safe?</h2>

  <ul class="services">
    <li><svg viewBox="0 0 14 14" aria-hidden="true"><circle cx="7" cy="7" r="6" fill="none" stroke="#666" stroke-width="1"/><path d="M4 7l2.2 2.2L11 3.5" stroke="var(--orange-deep)" stroke-width="1.6" fill="none"/></svg><span>K M Guard Solutions install, maintain and repair all intruder alarms, CCTV, intercom and access control</span></li>
    <li><svg viewBox="0 0 14 14" aria-hidden="true"><circle cx="7" cy="7" r="6" fill="none" stroke="#666" stroke-width="1"/><path d="M4 7l2.2 2.2L11 3.5" stroke="var(--orange-deep)" stroke-width="1.6" fill="none"/></svg><span>View, control and manage your security systems anywhere in the world</span></li>
    <li><svg viewBox="0 0 14 14" aria-hidden="true"><circle cx="7" cy="7" r="6" fill="none" stroke="#666" stroke-width="1"/><path d="M4 7l2.2 2.2L11 3.5" stroke="var(--orange-deep)" stroke-width="1.6" fill="none"/></svg><span>Feel at ease with monitoring services &amp; police response tailored to suit you and your business</span></li>
    <li><svg viewBox="0 0 14 14" aria-hidden="true"><circle cx="7" cy="7" r="6" fill="none" stroke="#666" stroke-width="1"/><path d="M4 7l2.2 2.2L11 3.5" stroke="var(--orange-deep)" stroke-width="1.6" fill="none"/></svg><span>K M Guard can takeover any existing security system and offer maintenance checks to guarantee the best performance for you and your premises</span></li>
    <li><svg viewBox="0 0 14 14" aria-hidden="true"><circle cx="7" cy="7" r="6" fill="none" stroke="#666" stroke-width="1"/><path d="M4 7l2.2 2.2L11 3.5" stroke="var(--orange-deep)" stroke-width="1.6" fill="none"/></svg><span>K M Guard understand that being security conscious is ever increasing, protecting your property and family is a number one priority</span></li>
    <li><svg viewBox="0 0 14 14" aria-hidden="true"><circle cx="7" cy="7" r="6" fill="none" stroke="#666" stroke-width="1"/><path d="M4 7l2.2 2.2L11 3.5" stroke="var(--orange-deep)" stroke-width="1.6" fill="none"/></svg><span>Our fully insured and accredited team offer quality, safety and cost efficiency throughout the whole process</span></li>
    <li><svg viewBox="0 0 14 14" aria-hidden="true"><circle cx="7" cy="7" r="6" fill="none" stroke="#666" stroke-width="1"/><path d="M4 7l2.2 2.2L11 3.5" stroke="var(--orange-deep)" stroke-width="1.6" fill="none"/></svg><span>K M Guard Solutions are using the latest cloud-based technology to stay connected with your home and business 24/7</span></li>
  </ul>

  <div class="accreditation">
    <span class="listing">Tradevouch.com</span>
    <span class="badge" aria-label="NQPB intruder alarm systems certificate"></span>
    <span class="badge badge--square" aria-label="Accreditation certificate"></span>
    <span class="badge" aria-label="NQPB CCTV systems certificate"></span>
  </div>

  <p class="callout">If you are looking to improve the security in your home, office or commercial property<br>then call a member of our team today for a free quote.</p>

  <footer class="footer">
    <div class="footer__phone">
      <svg width="18" height="18" viewBox="0 0 24 24" aria-hidden="true"><circle cx="12" cy="12" r="10.5" fill="none" stroke="#fff" stroke-width="1.8"/><path d="M8.2 6.5l2 2.2-1.1 1.6c.8 1.7 2 2.9 3.7 3.7l1.6-1.1 2.2 2-1.3 2c-4.4-.4-8.1-4.1-8.5-8.5z" fill="#fff"/></svg>
      01632 480913
    </div>
    <div class="footer__band">
      <div>operations@kmguardsolutions.co.uk &nbsp;|&nbsp; www.kmguardsolutions.co.uk</div>
      <div class="footer__address">14 Harlow Lane, Brentwood, Essex, CM14 9QX</div>
    </div>
  </footer>
</section>

</body>
</html>
```